依頼詳細
メルマガ登録用のランディングページをお願いします。概要に書かせて頂いた通り、
変わるきっかけが欲しいけどなかなか行動できない方たちが、
作成していただいたLPから可能性を感じて、
ここなら変われるかも知れないと期待感が湧きでるような、
未来を想像して興奮してしまうような感じでお願いします。
ファーストインプレッションは大事にしたいです。

スマホとPCのどちらでも見られるような大きさでお願いします。
サイトURL
http://hanabira-tsumugi.com/lp/
ページ数
1ページ
希望イメージ
シンプル 複雑
単色 カラフル
暗い 明るい
日常 高級
遊び心 厳粛
未来的 伝統的
女性的 男性的
希望する色
納品ファイル
補足説明
作成していただいたLP内の文章などあとで、
wordpressで編集できるようにしていただきたいです。
初めての依頼なので、作成していただく時点で不明点などあれば、
すぐに追記させていただきます!!!
提案の締め切りを1日のばしました。
みなさまのご提案楽しみにしております。
■ 選んだ理由

ファーストインパクトが気に入りました。

■ 提案者全員のお礼・コメント

初心者の提案でも丁寧に提案していただきみなさまありがとうございます。

```html
<!DOCTYPE html>
<html lang="ja">
<head>
<meta charset="utf-8">
<title>彼女いない歴＝自分の年齢だった僕が</title>
<link href="https://fonts.googleapis.com/css2?family=Noto+Sans+JP:wght@400;500;700&family=Dela+Gothic+One&family=Shippori+Mincho+B1:wght@800&display=swap" rel="stylesheet">
<style>
  :root{
    --header-red:#a80000;
    --header-deep:#5c0000;
    --wine:#4a0707;
    --wine-deep:#2a0202;
    --white:#ffffff;
    --ink:#1a1a1a;
    --yellow:#ffe400;
    --soft-yellow:#fff36b;
    --gold:#d9b24a;
    --gold-light:#f5dc8a;
    --panel:#160d0c;
    --panel-line:#6b5530;
  }
  *{margin:0;padding:0;box-sizing:border-box}
  html,body{width:1200px;height:4652px;overflow:hidden}
  body{
    position:relative;
    font-family:"Noto Sans JP",sans-serif;
    background:linear-gradient(180deg,var(--wine) 0%,var(--wine-deep) 45%,var(--wine) 100%);
    color:var(--white);
  }
  .hero-head{
    position:absolute;left:0;top:0;width:1200px;height:460px;
    background:linear-gradient(180deg,var(--header-red) 0%,var(--header-deep) 100%);
  }
  .hero-title{
    position:absolute;left:40px;top:28px;
    font-weight:500;font-size:188px;line-height:210px;letter-spacing:2px;
    color:var(--white);
  }
  .hero-photo{
    position:absolute;left:0;top:460px;width:1200px;height:560px;
    background:linear-gradient(180deg,#ffffff 0%,#f3f1ef 60%,#e4e0dc 100%);
  }
  .hero-title-end{
    position:absolute;left:20px;top:455px;
    font-weight:500;font-size:210px;line-height:230px;letter-spacing:8px;
    color:var(--ink);
  }
  .lead{
    position:absolute;left:48px;top:1040px;width:1120px;
    font-weight:500;font-size:94px;line-height:112px;letter-spacing:-1px;
  }
  .lead em{font-style:normal;color:var(--yellow)}
  .signup{
    position:absolute;left:140px;width:920px;height:488px;
    background:var(--panel);border:3px solid var(--panel-line);
  }
  .signup-1{top:1720px}
  .signup-2{top:4240px;height:440px}
  .signup-title{
    display:flex;align-items:center;justify-content:center;gap:40px;
    height:130px;border-bottom:2px solid var(--panel-line);
    font-family:"Shippori Mincho B1",serif;font-weight:800;font-size:60px;
    color:var(--gold-light);letter-spacing:4px;
  }
  .signup-title svg{width:56px;height:40px}
  .field{display:flex;align-items:center;justify-content:flex-end;gap:36px;padding-right:26px;margin-top:44px}
  .field label{font-size:40px;color:var(--white)}
  .field span{display:block;width:510px;height:84px;background:var(--white);border-radius:8px}
  .story{
    position:absolute;left:160px;top:2292px;width:900px;
    font-size:33px;line-height:35.5px;color:var(--soft-yellow);white-space:pre-line;
  }
  .catch{
    position:absolute;left:60px;top:3140px;width:1080px;text-align:center;
    font-family:"Dela Gothic One",sans-serif;font-size:106px;line-height:146px;
    color:var(--yellow);
    -webkit-text-stroke:3px #3a2400;
    text-shadow:0 0 18px #fff27a,0 0 40px #ffd400,0 0 70px rgba(255,200,0,.7);
  }
  .closing{
    position:absolute;left:160px;top:3940px;width:900px;
    font-size:33px;line-height:44px;color:var(--soft-yellow);
  }
</style>
</head>
<body>
  <header class="hero-head">
    <h1 class="hero-title">彼女いない歴<br>＝自分の年齢</h1>
  </header>
  <div class="hero-photo" role="img" aria-label="ピースサインをする笑顔の男性と女性の写真"></div>
  <p class="hero-title-end">だった僕が</p>

  <p class="lead">勘違いしていた<em>恋愛観</em>を<br><em>180</em>度変えてみたら、<br>あっさり<em>彼女</em>が出来た。<br>その方法を<em>まとめた</em>ので<br>一度読んでみて下さい。</p>

  <section class="signup signup-1">
    <h2 class="signup-title">
      <svg viewBox="0 0 56 40"><circle cx="28" cy="20" r="12" fill="none" stroke="#d9b24a" stroke-width="3"/></svg>
      無料メルマガ登録
      <svg viewBox="0 0 56 40"><circle cx="28" cy="20" r="12" fill="none" stroke="#d9b24a" stroke-width="3"/></svg>
    </h2>
    <div class="field"><label>お名前</label><span></span></div>
    <div class="field"><label>メールアドレス</label><span></span></div>
  </section>

  <p class="story">ある事がきっかけで、女の子と仲良くなれる方法を知り、
少しずつ実践していった結果・・・

あれだけ自信が無かった自分が、徐々にだが
“生まれ変わっている”とじわじわ実感でき、
ついには女の子とデート出来るまでこれた。

それが、たった1ヶ月で。

僕は今までなんでモテなかったんだろう・・・
そんな理由はすぐにわかった。なぜなら、
失敗をすることが恐くて、何もしてなかったからだ。
どうせモテもしないのに、お金も時間も使って
なにが楽しいんだと。

じゃあ、その無駄なお金と時間を使って失敗した経験を
先に知っておけば楽してモテるんじゃね？
と思うじゃ無いですか！
でもね。恋愛ハウツー本とか買うだけ無駄！

だって、恋愛のテクニックばかりが書いていて、
誰もが真似出来るコトじゃないから。</p>

  <p class="catch">本気でモテまくるには<br>テクニックじゃない。<br>重要なのはマインド！</p>

  <p class="closing">恋愛で重要なことをまとめました！<br>実体験から学んだ、恋愛マインドを誰でも簡単に<br>実践出来る方法は無料メルマガで読めます！</p>

  <section class="signup signup-2">
    <h2 class="signup-title">
      <svg viewBox="0 0 56 40"><circle cx="28" cy="20" r="12" fill="none" stroke="#d9b24a" stroke-width="3"/></svg>
      無料メルマガ登録
      <svg viewBox="0 0 56 40"><circle cx="28" cy="20" r="12" fill="none" stroke="#d9b24a" stroke-width="3"/></svg>
    </h2>
    <div class="field"><label>お名前</label><span></span></div>
    <div class="field"><label>メールアドレス</label><span></span></div>
  </section>
</body>
</html>
```